Business card design needed

Special effects makeup artist.
I would love it to have my own photos on it. Because I do both SPFX (ghor) and beauty I would like the card on one side to be beauty and the other side SPFX.

If both sides can not be done that is fine, I still want it to represent BOTH sides of what I do paying more attention to the GHOR aspect please as its what I specialise in.

Its not letting me upload any photos but please go to

WWW.EXAMPLEBOOK.NET/VANTEFXART
As that's where my photos (well most of) are located. There is HEAPS of ghor on there.

Industry/Entity Type

Business

Contact Information for Business Card

Vante Quillmere ~ Makeup Artist Extraordinaire.
0491237785
MissQuillmere@mailnest.net
WWW.Examplebook.net/VanteFXArt

Logo Text

Vante Quillmere

Logo styles of interest
Wordmark Logo
Requirements
Must have
• My Photos
Blood Dripping
Nice to have
• My Photos
Zombie kind of design
Blood dripping writing
Lots of greens and reds
Should not have
• Flowers, swirls or REALLY girly things

```html
<!DOCTYPE html>
<html lang="en">
<head>
<meta charset="utf-8">
<title>Vante Quillmere – Business Card</title>
<link rel="stylesheet" href="https://fonts.googleapis.com/css2?family=Arimo:wght@400;700&display=swap">
<style>
  :root {
    --ink-night: #0b0d12;
    --ink-shadow: #151a22;
    --blood-dark: #5a1a18;
    --blood-mid: #8a2a24;
    --blood-bright: #f0141c;
    --slime-green: #8fe51b;
    --paper-white: #ffffff;
    --icon-blue: #3b5cb8;
  }
  * { margin: 0; padding: 0; box-sizing: border-box; }
  html, body {
    width: 1200px;
    height: 693px;
    overflow: hidden;
    background: var(--ink-night);
  }
  .card {
    position: relative;
    width: 1200px;
    height: 693px;
    overflow: hidden;
    font-family: "Arimo", Arial, sans-serif;
    color: var(--paper-white);
  }
  .card__photo {
    position: absolute;
    inset: 0;
    background:
      radial-gradient(ellipse 360px 300px at 900px 380px, var(--blood-mid) 0%, var(--blood-dark) 40%, transparent 75%),
      radial-gradient(ellipse 520px 420px at 300px 250px, var(--ink-shadow) 0%, transparent 80%),
      linear-gradient(135deg, #11151c 0%, var(--ink-night) 60%, #07080b 100%);
  }
  .card__band {
    position: absolute;
    top: 0;
    left: 0;
    width: 1200px;
    height: 15px;
    background: var(--blood-bright);
  }
  .card__drip-art {
    position: absolute;
    top: 0;
    right: 0;
    width: 275px;
    height: 192px;
    background: linear-gradient(to bottom, var(--blood-bright) 0%, var(--blood-bright) 35%, rgba(240, 20, 28, 0.35) 100%);
  }
  .wordmark {
    position: absolute;
    left: 60px;
    top: 150px;
    color: var(--slime-green);
    font-weight: 700;
    font-size: 112px;
    line-height: 1;
    letter-spacing: -2px;
  }
  .wordmark__line { display: block; }
  .wordmark__line--second { margin-left: 110px; margin-top: 10px; }
  .tagline {
    position: absolute;
    left: 41px;
    top: 466px;
    font-size: 28px;
    font-weight: 700;
    letter-spacing: 0.3px;
  }
  .contact {
    position: absolute;
    left: 41px;
    top: 516px;
    list-style: none;
    font-size: 27px;
    font-weight: 400;
  }
  .contact__item {
    display: flex;
    align-items: center;
    height: 40px;
  }
  .contact__label { width: 80px; }
  .contact__icon {
    width: 34px;
    height: 34px;
    border-radius: 6px;
    background: var(--icon-blue);
    margin-left: -6px;
    margin-right: 52px;
  }
</style>
</head>
<body>
  <main class="card">
    <div class="card__photo" role="img" aria-label="Dark photograph of a gore special effects makeup model covered in blood, posed against plastic sheeting"></div>

    <div class="card__band" aria-hidden="true"></div>
    <div class="card__drip-art" role="img" aria-label="Red dripping blood graphic running down from the top edge"></div>

    <h1 class="wordmark">
      <span class="wordmark__line">Vante</span>
      <span class="wordmark__line wordmark__line--second">Quillmere</span>
    </h1>

    <p class="tagline">MAKEUP ARTIST EXTRAORDINAIRE</p>

    <ul class="contact">
      <li class="contact__item"><span class="contact__label">T:</span><span>0491237785</span></li>
      <li class="contact__item"><span class="contact__label">E:</span><span>MissQuillmere@mailnest.net</span></li>
      <li class="contact__item"><span class="contact__icon" aria-hidden="true"></span><span>www.examplebook.net/VanteFXArt</span></li>
    </ul>
  </main>
</body>
</html>
```